New word press website site design

We provide email marketing to aircraft brokers and dealers to assist in finding buyers for their aircraft.

Our target market to purchase our broadcasts are the aircraft sellers – NOT the buyers.

Our target market when sending the email broadcast, are the buyers (end users).

The website should target brokers and our email database targets the buyers.

We do not buy or sell aircraft as a company. We provide email marketing solutions to connect buyers and sellers of aircraft.

Our other site is vesseltrove.net and will be redesigned soon. Please use it as a reference as far as general scope but they layout can be completely different and should include helicopters only as far as imagery. The colors should be similar as the logos are similar, however we do NOT want both sites to be identical in use of primary color

Plenty of images and sample broadcasts attached to use as needed throughout the site.

Headlines listed below with some text copy.

In the event that we need to add more text, please use standard greek text as a place holder for the purposes of the mockup design.

Need to have a “SUBSCRIBE” button to join our mailing list.

Possible Headlines:

Exclusively Showcasing Rotor Wing Aircraft to the Global Marketplace

Showcasing Pre-Owned Helicopters Available For Sale, Lease, Trade, or Wanted for Acquisition.

Mobile-optimized Email Campaigns that Render Correctly Across all Devices

Targeted worldwide recipients that currently own, operate, or have an interest in rotor wing aircraft

STRONGEST Rotor Wing Database in the Industry

Text/Copy:

HOME
Rotorline Parade is one of most powerful marketing tools in the industry to utilize in reaching targeted buyers of pre-owned helicopters. Rotorline Parade provides the rotor wing aircraft market with a fast, effective, and affordable email broadcast solution to utilize in the marketing of Helicopters for sale.

Developed Exclusively to Parade Rotor Wing Aircraft to the Global marketplace, Rotorline Parade is a powerful tool designed to maximize leads and accelerate the sales process by providing the ability to reach a global network of Helicopter buyers in a matter of seconds.

DATABASE:

While Rotorline Parade is delivered to all known broker/dealers, our primary focus is in reaching end users. Our opt-in/opt-out recipient database is updated daily and developed specifically to deliver the latest details on helicopters available for sale or lease to the inboxes of a global network of Helicopter buyers and sellers.

· Helicopter Owners

· Helicopter Operators

· Helicopter Charter Services

· Helicopter Management Companies

· Corporate/Municipal Flight Departments

· Helicopter Pilots

· Senior Aviation Executives

· Wealth Management Firms

· High Net Worth Individuals

· Helicopter Broker/Dealers

Helicopter Tour/Travel Firms

· Off Shore Oil & Gas Production Firms

· Municipalities/Media/Medevac Firms

Our recipient database is continuously updated and developed specifically to reach buyers and sellers of Helicopters. This ensures that your Helicopter will be showcased to the right people. Rotorline Parade does not broadcast non-rotor wing aircraft and focuses exclusively on the Global Helicopter Market.

Broadcast Design:

Rotorline Parade broadcast ads are custom designed for you by incorporating your corporate image and branding. Because you have worked hard in developing your corporate image, we strive to maintain it while designing an ad that will showcase your Helicopter to its best advantage. Rotorline Parade utilizes Mobile-optimized Email Campaigns with Responsive Coding to render correctly across all devices

Once you have approved the design, we schedule the broadcast to be sent on the available date and time you request. The broadcast will link to your website and the results can be immediate. All email leads and replies will go to the email address that you provided.

Pricing:
Create a place holder for 3 Different Broadcast Packages

-Broadcast Package A
-Broadcast Package B
-Broadcast Package C

Target Market(s)

The target market is any person or company that has aircraft for sale. We work with brokers, dealers, and owners to assist in finding buyers for their aircraft using email marketing campaigns (Parade broadcasts).

Industry/Entity Type

Aviation

Colors
0255a3
00a990

Requirements
Nice to have
• Samples of helicopter for sale broadcast ads in /image gallery/slider

```html
<!DOCTYPE html>
<html lang="en">
<head>
<meta charset="utf-8">
<title>Rotorcraft Reach Inc – Rotorline Parade</title>
<link href="https://fonts.googleapis.com/css2?family=Lato:wght@400;700;900&display=swap" rel="stylesheet">
<style>
  :root {
    --navy: #1c2a6e;
    --navy-deep: #142058;
    --gold: #f0b81c;
    --ink: #222631;
    --white: #ffffff;
    --card: #e9e9eb;
    --black: #050608;
  }
  * { box-sizing: border-box; margin: 0; padding: 0; }
  html, body { width: 1200px; height: 3550px; overflow: hidden; }
  body { font-family: "Lato", Arial, sans-serif; color: var(--ink); background: var(--white); position: relative; }

  .site-header { height: 173px; display: flex; align-items: center; justify-content: center; gap: 22px; }
  .brand-dot { width: 96px; height: 96px; border-radius: 50%; background: var(--navy); }
  .brand-name { font-weight: 900; font-size: 30px; color: var(--navy); letter-spacing: 1px; }

  .hero { position: relative; height: 603px; background: var(--black); overflow: hidden; }
  .hero-photo { position: absolute; inset: 0;
    background: radial-gradient(ellipse 55% 40% at 52% 68%, #9a9ea6 0%, #4d525a 35%, #15171b 70%, var(--black) 100%); }
  .hero-title { position: relative; text-align: center; color: var(--white); font-weight: 900;
    font-size: 51px; line-height: 59px; padding-top: 40px; }
  .btn { display: inline-block; background: var(--gold); color: var(--black); font-weight: 700;
    border-radius: 40px; text-align: center; text-decoration: none; }
  .hero-btn { position: absolute; left: 472px; top: 170px; width: 256px; height: 64px; line-height: 64px; font-size: 24px; letter-spacing: 1px; }

  .gallery-strip { display: block; margin-top: 10px; }

  .about { padding: 62px 50px 0; text-align: center; height: 516px; }
  .section-title { font-weight: 900; font-size: 52px; line-height: 60px; color: var(--navy); }
  .about p { font-size: 24px; line-height: 42px; margin: 22px auto 0; max-width: 1100px; }
  .about p + p { margin-top: 26px; }

  .database { position: relative; height: 990px; color: var(--white); text-align: center; overflow: hidden; }
  .database-photo { position: absolute; inset: 0;
    background: radial-gradient(ellipse 40% 35% at 28% 30%, #3a4a7c 0%, transparent 70%),
                radial-gradient(ellipse 45% 40% at 75% 75%, #33446f 0%, transparent 70%),
                linear-gradient(180deg, #1d2c66 0%, #1a2a68 100%); }
  .database-inner { position: relative; padding: 52px 40px 0; }
  .database .section-title { color: var(--white); }
  .database p { font-size: 24px; line-height: 42px; max-width: 1130px; margin: 22px auto 0; }
  .audience { list-style: none; position: relative; height: 400px; margin-top: 42px; text-align: left; }
  .audience li { position: absolute; font-size: 24px; line-height: 36px; padding-left: 58px; }
  .audience li svg { position: absolute; left: 0; top: 7px; }
  .database .closing { margin-top: 0; }

  .pricing { text-align: center; padding-top: 62px; height: 887px; }
  .pricing-sub { font-size: 24px; margin-top: 18px; }
  .packages { position: relative; margin-top: 0; height: 600px; }
  .package { position: absolute; top: 64px; width: 360px; height: 568px; background: var(--card); border-radius: 34px; overflow: hidden; }
  .package-head { position: relative; height: 190px; background: radial-gradient(ellipse 60% 60% at 50% 70%, #4a4f58 0%, #17191d 70%, #0b0c0e 100%); }
  .package-title { position: absolute; left: 0; right: 0; top: 30px; color: var(--white); font-weight: 900; font-size: 34px; line-height: 42px; }
  .package-title span { display: block; color: var(--gold); }
  .price { position: absolute; left: 109px; top: 137px; width: 142px; height: 142px; border-radius: 50%;
    background: var(--navy); border: 5px solid var(--white); color: var(--white); }
  .price-amount { display: block; font-size: 50px; font-weight: 700; line-height: 50px; margin-top: 26px; }
  .price-amount sup { font-size: 22px; vertical-align: 22px; }
  .price-term { display: block; font-size: 32px; font-style: italic; line-height: 34px; }
  .package-text { position: absolute; top: 305px; left: 40px; right: 40px; font-size: 24px; line-height: 41px; }
  .package-btn { position: absolute; left: 66px; top: 483px; width: 228px; height: 58px; line-height: 58px; font-size: 24px; }

  .site-footer { position: absolute; left: 0; top: 3368px; width: 1200px; height: 182px; background: var(--navy); color: var(--white); }
  .footer-badge { position: absolute; left: 552px; top: -52px; width: 96px; height: 96px; border-radius: 50%; background: var(--white); }
  .copyright { position: absolute; left: 43px; top: 52px; font-size: 19px; }
  .social { position: absolute; left: 43px; top: 98px; display: flex; gap: 22px; list-style: none; }
  .social li { width: 32px; height: 32px; border-radius: 50%; background: var(--white); }
  .contact { position: absolute; right: 43px; top: 48px; text-align: right; }
  .contact .phone { display: block; font-size: 34px; font-weight: 700; line-height: 40px; }
  .contact .email { display: block; font-size: 22px; margin-top: 16px; }
</style>
</head>
<body>

<header class="site-header">
  <span class="brand-dot"></span>
  <span class="brand-name">ROTORCRAFT REACH INC</span>
</header>

<section class="hero">
  <div class="hero-photo" role="img" aria-label="Silver and black helicopter parked on a dark studio floor"></div>
  <h1 class="hero-title">Exclusively Showcasing Rotor Wing Aircraft<br>to the Global Marketplace</h1>
  <a class="btn hero-btn" href="#">SUBSCRIBE</a>
</section>

<svg class="gallery-strip" width="1200" height="189" viewBox="0 0 1200 189" role="img" aria-label="Gallery of three helicopters: over a city, on a blue sky, and at sunset">
  <defs>
    <linearGradient id="sky-city" x1="0" y1="0" x2="0" y2="1"><stop offset="0" stop-color="#9fb4c9"/><stop offset="1" stop-color="#3d4f63"/></linearGradient>
    <linearGradient id="sky-blue" x1="0" y1="0" x2="0" y2="1"><stop offset="0" stop-color="#2f6fc0"/><stop offset="1" stop-color="#1b3f7a"/></linearGradient>
    <linearGradient id="sky-dusk" x1="0" y1="0" x2="0" y2="1"><stop offset="0" stop-color="#3d4a6c"/><stop offset="0.6" stop-color="#d98a52"/><stop offset="1" stop-color="#2a2320"/></linearGradient>
  </defs>
  <polygon points="0,0 425,0 360,189 0,189" fill="url(#sky-city)"/>
  <polygon points="425,0 848,0 790,189 360,189" fill="url(#sky-blue)"/>
  <polygon points="848,0 1200,0 1200,189 790,189" fill="url(#sky-dusk)"/>
  <line x1="425" y1="0" x2="360" y2="189" stroke="#fff" stroke-width="8"/>
  <line x1="848" y1="0" x2="790" y2="189" stroke="#fff" stroke-width="8"/>
</svg>

<section class="about">
  <h2 class="section-title">About Rotorcraft Reach Inc.</h2>
  <p>Rotorline Parade is one of most powerful marketing tools in the industry to utilize in reaching targeted buyers of pre-owned helicopters. Rotorline Parade provides the rotor wing aircraft market with a fast, effective, and affordable email broadcast solution to utilize in the marketing of Helicopters for sale.</p>
  <p>Developed Exclusively to Parade Rotor Wing Aircraft to the Global marketplace, Rotorline Parade is a powerful tool designed to maximize leads and accelerate the sales process by providing the ability to reach a global network of Helicopter buyers in a matter of seconds.</p>
</section>

<section class="database">
  <div class="database-photo" role="img" aria-label="Dark blue toned photo of helicopters on a landing pad"></div>
  <div class="database-inner">
    <h2 class="section-title">Database</h2>
    <p>While Rotorline Parade is delivered to all known broker/dealers, our primary focus is in reaching end users. Our opt-in/opt-out recipient database is updated daily and developed specifically to deliver the latest details on helicopters available for sale or lease to the inboxes of a global network of Helicopter buyers and sellers.</p>
    <ul class="audience">
      <li style="left:46px;top:0">Helicopter Owners</li>
      <li style="left:46px;top:52px">Helicopter Operators</li>
      <li style="left:46px;top:104px">Helicopter Charter Services</li>
      <li style="left:46px;top:156px">Helicopter Management Companies</li>
      <li style="left:46px;top:208px">Corporate/Municipal Flight Departments</li>
      <li style="left:46px;top:260px">Helicopter Pilots</li>
      <li style="left:46px;top:312px">Senior Aviation Executives</li>
      <li style="left:606px;top:0">Wealth Management Firms</li>
      <li style="left:606px;top:52px">High Net Worth Individuals</li>
      <li style="left:606px;top:104px">Helicopter Broker/Dealers</li>
      <li style="left:606px;top:156px">Helicopter Tour/Travel Firms</li>
      <li style="left:606px;top:208px">Off Shore Oil &amp; Gas Production Firms</li>
      <li style="left:606px;top:260px">Municipalities/Media/Medevac Firms</li>
    </ul>
    <p class="closing">Our recipient database is continuously updated and developed specifically to reach buyers and sellers of Helicopters. This ensures that your Helicopter will be showcased to the right people. Rotorline Parade does not broadcast non-rotor wing aircraft and focuses exclusively on the Global Helicopter Market.</p>
  </div>
</section>

<section class="pricing">
  <h2 class="section-title">Pricing</h2>
  <p class="pricing-sub">3 Different Broadcast Packages:</p>
  <div class="packages">
    <article class="package" style="left:43px">
      <div class="package-head" role="img" aria-label="Helicopter on a dark background"></div>
      <h3 class="package-title">Broadcast Package<span>A</span></h3>
      <div class="price"><span class="price-amount"><sup>$</sup>120</span><span class="price-term">pm</span></div>
      <p class="package-text">Aliquam molestie, mi et imperdiet euismod, dui purus auctor tellus neque ac lobortis volutpat</p>
      <a class="btn package-btn" href="#">Subscribe</a>
    </article>
    <article class="package" style="left:421px">
      <div class="package-head" role="img" aria-label="Helicopter on a dark background"></div>
      <h3 class="package-title">Broadcast Package<span>B</span></h3>
      <div class="price"><span class="price-amount"><sup>$</sup>180</span><span class="price-term">pm</span></div>
      <p class="package-text">Aliquam molestie, mi et imperdiet euismod, dui purus auctor tellus neque ac lobortis volutpat</p>
      <a class="btn package-btn" href="#">Subscribe</a>
    </article>
    <article class="package" style="left:798px">
      <div class="package-head" role="img" aria-label="Helicopter on a dark background"></div>
      <h3 class="package-title">Broadcast Package<span>C</span></h3>
      <div class="price"><span class="price-amount"><sup>$</sup>200</span><span class="price-term">pm</span></div>
      <p class="package-text">Aliquam molestie, mi et imperdiet euismod, dui purus auctor tellus neque ac lobortis volutpat</p>
      <a class="btn package-btn" href="#">Subscribe</a>
    </article>
  </div>
</section>

<footer class="site-footer">
  <span class="footer-badge"></span>
  <p class="copyright">© 2018. Rotorcraft Reach Inc. All Right Reserved</p>
  <ul class="social" aria-label="Social links">
    <li></li><li></li><li></li><li></li><li></li>
  </ul>
  <div class="contact">
    <span class="phone">1-800-555-0142</span>
    <span class="email">info@rotorcraftreach.com</span>
  </div>
</footer>

<svg width="0" height="0" style="position:absolute">
  <defs>
    <symbol id="tick" viewBox="0 0 22 22">
      <circle cx="11" cy="11" r="11" fill="#f0b81c"/>
      <path d="M6 11.5l3.4 3.4L16 8" fill="none" stroke="#1c2a6e" stroke-width="2.6" stroke-linecap="round" stroke-linejoin="round"/>
    </symbol>
  </defs>
</svg>
<style>
  .audience li::before { content: ""; position: absolute; left: 0; top: 7px; width: 22px; height: 22px; border-radius: 50%; background: var(--gold); }
  .audience li::after { content: ""; position: absolute; left: 6px; top: 12px; width: 9px; height: 5px; border-left: 3px solid var(--navy); border-bottom: 3px solid var(--navy); transform: rotate(-45deg); }
</style>
</body>
</html>
```